Agrarhandel benötigt Homepage
Zielgruppe
Wir sind ein Agrarhandel mit einem Warenumschlagslager im Sinne eines klassischen Einzelhandels und vertreiben Produkte an Landwirte.
Wir vertreiben folgende Hauptproduktgruppen:
Einzelfuttermittel
wie z.B. Sojaexktraktionsschrot. Die einzelnen Produkte könnten z.B. wie die Futtermittel auf folgender Seite dargestellt werden (https://www.kornblick.eu/de/produkt/heltrosamin)
Mischfuttermittel
Hier bieten wir unseren Kunden an, individuelles Mischfutter auf Basis unserer Einzelfuttermittel herzustellen.
Weitere Details und weitere Produktbereiche habe ich in einer Powerpoint-Übersicht dargestellt.
Neben diesen Produkten wollen wir uns als Familienunternehmen selbst vorstellen. Zudem betreiben wir in unserer Familie zusätzlich einen Milchviehbetrieb den wir ebenfalls hervorheben möchten, da wir unseren Kunden gegenüber einerseits als Zulieferer aber auch als Kollege auftreten wollen.
Einzelfuttermittel: Hier können wir durch unsere Unabhängigkeit punkten, da wir nicht abhängig von bestimmten Lieferanten sind und dementsprechend unabhängig beraten können. Wir untersuchen im Vergleich zu unseren Wettbewerben die Qualität der Futtermittel bis ins Detail und können daher eine Transparenz bieten, die Konkurrenten in der Regel nicht bieten können. Unser Warenumschlagsplatz mit moderner Technik ermöglicht es uns äußerst kosteneffizient die Waren umschlagen und ausliefern zu können.
Mischfuttermittel: Auf Basis der vorhandenen Einzelfuttermittel stellen wir je nach Kundenwunsch individuelle Mischfutter her. Wir arbeiten mit offenen Deklarationen, sodass unsere Kunden jederzeit nachvollziehen können, ob auch die Einzelfuttermittel verwendet wurden, die sie bestellt haben und keine billigen Ersatzprodukte verwendet wurden.
Zudem sind wir ZP und BRUT zertifiziert. Die aktuellen für unser Unternehmen ausgestellten Zertifikate müssen für unsere Kunden als Download zur Verfügung stehen. Statt dem BRUT-Logo bitte das ..
Aufgabenstellung
Wir möchten gerne ein zeitgemäße Homepage, jedoch muss auch berücksichtigt werden, dass unsere Kunden eher konservativ denken.

```html
<!DOCTYPE html>
<html lang="de">
<head>
<meta charset="utf-8">
<title>Mischfuttermittel – Auen Landhandel</title>
<link href="https://fonts.googleapis.com/css2?family=Open+Sans:ital,wght@0,400;0,600;0,700;1,400&display=swap" rel="stylesheet">
<style>
:root{
  --green:#176b4e;
  --green-dark:#0d4735;
  --yellow:#f5b400;
  --ink:#2a2a3a;
  --white:#ffffff;
  --black:#050505;
  --straw-1:#efe6d6;
  --straw-2:#e3d3b8;
}
*{box-sizing:border-box;margin:0;padding:0}
html,body{width:668px;height:1200px;overflow:hidden;background:var(--white)}
body{position:relative;font-family:"Open Sans",Arial,sans-serif;color:var(--ink)}
.topbar{position:absolute;left:0;top:0;width:668px;height:21px;background:linear-gradient(90deg,var(--green-dark),var(--green));color:var(--white);font-size:7.4px;font-weight:600}
.topbar .cta{position:absolute;left:430px;top:5px}
.topbar .tel{position:absolute;left:548px;top:5px;display:flex;align-items:center;gap:5px}
.icon{width:11px;height:11px;border-radius:50%;background:var(--yellow);display:inline-flex;align-items:center;justify-content:center;flex:none}
.icon svg{width:7px;height:7px}
.nav{position:absolute;left:0;top:21px;width:668px;height:56px;background:var(--white);border-bottom:1px solid #e4e4e4}
.nav a{position:absolute;top:28px;font-size:7.4px;color:var(--ink);text-decoration:none;letter-spacing:.1px}
.nav a.active{font-weight:700}
.nav .underline{position:absolute;left:158px;top:52px;width:76px;height:3px;background:var(--green)}
.burger{position:absolute;left:597px;top:28px;width:15px}
.burger span{display:block;height:1.4px;background:var(--ink);margin-bottom:2.3px}
.hero{position:absolute;left:0;top:77px;width:668px;height:314px;background:linear-gradient(100deg,#b97a45 0%,#8a5a38 30%,#4a3a33 55%,#6b5a50 75%,#3a2d28 100%)}
.brand-badge{position:absolute;left:280px;top:11px;width:108px;height:108px;border-radius:50%;background:var(--white);display:flex;align-items:center;justify-content:center;text-align:center;color:var(--green);font-weight:700;font-size:10px;line-height:1.2;z-index:2}
.intro{position:absolute;left:0;top:418px;width:668px;text-align:center}
.intro h1{font-size:24px;line-height:31px;font-weight:700;color:var(--green);letter-spacing:.3px}
.intro p{margin:27px auto 0;width:290px;font-size:7.9px;line-height:11.5px}
.phone-btn{position:absolute;left:268px;top:562px;width:134px;height:26px;border-radius:6px;background:var(--green);color:var(--white);display:flex;align-items:center;padding-left:11px;gap:12px;font-size:11.5px}
.phone-btn .icon{width:16px;height:16px}
.phone-btn .icon svg{width:9px;height:9px}
.spec{position:absolute;left:19px;top:611px;width:630px;height:307px;padding:2px;background:linear-gradient(135deg,var(--straw-1),var(--straw-2) 50%,var(--straw-1))}
.spec table{width:626px;border-collapse:collapse;border:1.6px solid #111;font-family:Arial,Helvetica,sans-serif;font-size:6.3px;color:#111;table-layout:fixed}
.spec td,.spec th{border-left:1px solid #222;text-align:center;padding:0;height:10px;line-height:10px}
.spec th{font-size:7.4px;font-weight:700;line-height:9.6px;height:44px;vertical-align:middle}
.spec td.label{text-align:left;padding-left:1.5px;border-left:none}
.spec td.label span{float:right;padding-right:2px}
.spec tr.art td{border-top:1px solid #222;font-weight:700;height:9px;line-height:9px}
.spec tr.art td.label{font-size:7px}
.spec tr.struct td{font-style:italic;font-size:5.2px;height:7px;line-height:7px;border-top:1px solid #222;border-bottom:1px solid #222}
.spec tr.section td{font-style:italic;font-weight:700;font-size:7.2px;height:11px;line-height:11px}
.spec tr.energy td{border-top:1.6px solid #111;font-weight:700;font-size:7.6px;height:15px}
.spec tr.data td{border-top:.6px solid #555}
.spec col.lbl{width:115px}
.footer{position:absolute;left:0;top:952px;width:668px;height:190px;background:linear-gradient(90deg,var(--green-dark),var(--green));color:var(--white)}
.footer .col{position:absolute;top:0;height:190px}
.f-brand{left:0;width:275px;text-align:center}
.f-info{left:275px;width:118px;border-left:1px solid rgba(255,255,255,.5);border-right:1px solid rgba(255,255,255,.5);text-align:center}
.f-about{left:393px;width:275px;text-align:center}
.f-brand .mark{width:26px;height:26px;border-radius:50%;border:1.5px solid var(--white);margin:34px auto 0}
.f-brand .name{margin-top:10px;font-size:11px;font-weight:600;letter-spacing:.2px}
.f-brand .addr{margin-top:12px;font-size:7.6px;line-height:9.5px}
.contacts{position:absolute;left:62px;top:140px;font-size:7.6px;display:grid;grid-template-columns:78px auto;row-gap:5px;column-gap:0;text-align:left}
.contacts div{display:flex;align-items:center;gap:5px}
.footer h2{font-size:8px;font-weight:700;letter-spacing:.2px;margin-top:29px}
.f-info ul{list-style:none;font-size:7.6px;line-height:9.9px;margin-top:44px}
.f-info ul+ul{margin-top:10px}
.f-about p{font-style:italic;font-size:6.7px;line-height:10.2px;width:160px;margin:29px auto 0}
.copyright{position:absolute;left:0;top:1142px;width:668px;height:24px;background:var(--black);color:var(--white);font-size:7.4px;text-align:center;line-height:24px}
</style>
</head>
<body>
<header>
  <div class="topbar">
    <span class="cta">Jetzt telefonisch beraten lassen</span>
    <span class="tel"><span class="icon"><svg viewBox="0 0 24 24"><path fill="#fff" d="M6.6 10.8a15 15 0 0 0 6.6 6.6l2.2-2.2c.3-.3.7-.4 1-.2 1.1.4 2.3.6 3.6.6.6 0 1 .4 1 1V20c0 .6-.4 1-1 1A17 17 0 0 1 3 4c0-.6.4-1 1-1h3.5c.6 0 1 .4 1 1 0 1.3.2 2.5.6 3.6.1.3 0 .7-.2 1z"/></svg></span>09123 456780</span>
  </div>
  <nav class="nav">
    <a style="left:56px">EINZELFUTTERMITTEL</a>
    <a class="active" style="left:158px">MISCHFUTTERMITTEL</a>
    <span class="underline"></span>
    <a style="left:404px">ÜBER UNS</a>
    <a style="left:463px">UNSER BETRIEB</a>
    <a style="left:540px">KONTAKT</a>
    <div class="burger"><span></span><span></span><span></span></div>
  </nav>
  <div class="brand-badge">Auen<br>Landhandel</div>
</header>

<div class="hero" role="img" aria-label="Foto: Milchkühe im warm beleuchteten Stall fressen am Futtertisch"></div>

<section class="intro">
  <h1>FUTTER INDIVIDUELL<br>MISCHEN LASSEN</h1>
  <p>Bei Bedarf mischen wir für Sie individuell das perfekte Mischfutter für Ihre Tiere basierend auf deren Energie- und Nährwertbedarf. Gerne beraten wir Sie hierzu ausführlich am Telefon.</p>
</section>

<a class="phone-btn"><span class="icon"><svg viewBox="0 0 24 24"><path fill="#fff" d="M6.6 10.8a15 15 0 0 0 6.6 6.6l2.2-2.2c.3-.3.7-.4 1-.2 1.1.4 2.3.6 3.6.6.6 0 1 .4 1 1V20c0 .6-.4 1-1 1A17 17 0 0 1 3 4c0-.6.4-1 1-1h3.5c.6 0 1 .4 1 1 0 1.3.2 2.5.6 3.6.1.3 0 .7-.2 1z"/></svg></span>09123 45 67 80</a>

<div class="spec">
<table>
<colgroup><col class="lbl"><col span="13"></colgroup>
<tr><th></th><th>Rind-Mix<br>28/4 K</th><th>Rind-Mix<br>Raps-<br>Plus</th><th>Rind-Mix<br>33/3 R</th><th>Rind-Mix<br>34/4 K</th><th>Rind-Mix<br>35/4 B</th><th>Rind-Mix<br>36 S</th><th>Rind-Mix<br>38/4 R</th><th>Rind-Mix<br>38/4<br>Extra</th><th>Rind-Mix<br>40/4 L</th><th>Rind-Mix<br>40/4 K</th><th>Rind-Mix<br>43/4 K</th><th>Rind-Mix<br>Bypass<br>Top K</th><th>Rind-Mix<br>Bypass<br>40 K</th></tr>
<tr class="art"><td class="label">Artikel-Nr.</td><td>710100/-20</td><td>710200/-20</td><td>710300/-20</td><td>710400/-20</td><td>710500/-20</td><td>710600</td><td>711700/-20</td><td>711800/-20</td><td>712100/-20</td><td>712200/-20</td><td>712300/-20</td><td>713200/-20</td><td>713300/-20</td></tr>
<tr class="struct"><td class="label">Futterstruktur:</td><td>mehlig/pell.</td><td>mehlig/pell.</td><td>mehlig/pell.</td><td>mehlig/pell.</td><td>mehlig/pell.</td><td>mehlig</td><td>mehlig/pell.</td><td>mehlig/pell.</td><td>mehlig/pell.</td><td>mehlig/pell.</td><td>mehlig/pell.</td><td>mehlig/pell.</td><td>mehlig/pell.</td></tr>
<tr class="section"><td class="label">Komponenten:</td><td></td><td></td><td></td><td></td><td></td><td></td><td></td><td></td><td></td><td></td><td></td><td></td><td></td></tr>
<tr class="data"><td class="label">europäischer Sojaschrot<span>%</span></td><td>45</td><td></td><td></td><td>38-40</td><td>15</td><td>33</td><td></td><td>30</td><td>7</td><td>47-49</td><td>57-60</td><td>40</td><td>56-58</td></tr>
<tr class="data"><td class="label">Rapsschrot/-kuchen<span>%</span></td><td>3-5</td><td>49</td><td>65-70</td><td>35-40</td><td>60-70</td><td>33</td><td>65-75</td><td>62-64</td><td>70-75</td><td>50-53</td><td>32-35</td><td></td><td>16-18</td></tr>
<tr class="data"><td class="label">geschützter Rapsschrot<span>%</span></td><td></td><td></td><td>20</td><td></td><td></td><td></td><td>10</td><td>5</td><td>5</td><td></td><td></td><td>59</td><td>25</td></tr>
<tr class="data"><td class="label">Leinschrot<span>%</span></td><td></td><td></td><td></td><td></td><td></td><td></td><td></td><td></td><td></td><td></td><td>5</td><td></td><td></td></tr>
<tr class="data"><td class="label">Maiskleberfutter/-schlempe, getr.<span>%</span></td><td></td><td>49</td><td>-15</td><td>-5</td><td>10-15</td><td>33</td><td>-20</td><td></td><td>-12</td><td></td><td></td><td></td><td></td></tr>
<tr class="data"><td class="label">Körnermais<span>%</span></td><td>24</td><td></td><td></td><td></td><td></td><td></td><td></td><td></td><td></td><td></td><td></td><td></td><td></td></tr>
<tr class="data"><td class="label">Melasseschnitzel<span>%</span></td><td>24</td><td></td><td></td><td>20</td><td></td><td></td><td></td><td></td><td></td><td></td><td></td><td></td><td></td></tr>
<tr class="data"><td class="label">Weizenkleie/-futtermehl<span>%</span></td><td></td><td></td><td>-5</td><td></td><td></td><td></td><td>-5</td><td></td><td></td><td></td><td></td><td></td><td></td></tr>
<tr class="data"><td class="label">Harnstoff<span>%</span></td><td></td><td></td><td></td><td></td><td></td><td></td><td>2,5</td><td></td><td>2,5</td><td></td><td></td><td></td><td></td></tr>
<tr class="data"><td class="label">Melasse/Vinasse<span>%</span></td><td>2-4</td><td>2</td><td>2-4</td><td>2-4</td><td>1-3</td><td>1</td><td>1-2</td><td>1-2</td><td>1-2</td><td>1-3</td><td>1-3</td><td>1</td><td>1-2</td></tr>
<tr class="section"><td class="label">Inhaltsstoffe:</td><td></td><td></td><td></td><td></td><td></td><td></td><td></td><td></td><td></td><td></td><td></td><td></td><td></td></tr>
<tr class="data"><td class="label">Rohprotein<span>%</span></td><td>28,0</td><td>30,5</td><td>33,0</td><td>34,0</td><td>35,0</td><td>36,0</td><td>38,0</td><td>38,0</td><td>40,0</td><td>40,0</td><td>42,0</td><td>38,0</td><td>40,5</td></tr>
<tr class="data"><td class="label">UDP<span>%</span></td><td>35</td><td>37</td><td>39</td><td>32</td><td>34</td><td>35</td><td>35</td><td>34</td><td>34</td><td>33</td><td>31</td><td>56</td><td>40</td></tr>
<tr class="data"><td class="label">nXP<span>g/kg</span></td><td>205</td><td>220</td><td>230</td><td>220</td><td>225</td><td>235</td><td>215</td><td>235</td><td>220</td><td>245</td><td>245</td><td>305</td><td>270</td></tr>
<tr class="data"><td class="label">RNB<span>g/kg</span></td><td>12</td><td>14</td><td>16</td><td>19</td><td>20</td><td>20</td><td>26</td><td>23</td><td>29</td><td>25</td><td>28</td><td>12</td><td>22</td></tr>
<tr class="data"><td class="label">Rohfett<span>%</span></td><td>2,5</td><td>6,0</td><td>3,0</td><td>3,0</td><td>3,5</td><td>4,5</td><td>4,0</td><td>3,0</td><td>3,0</td><td>3,0</td><td>2,5</td><td>2,5</td><td>2,5</td></tr>
<tr class="data"><td class="label">Rohfaser<span>%</span></td><td>6,5</td><td>9,0</td><td>11,0</td><td>9,0</td><td>9,5</td><td>7,5</td><td>10,0</td><td>8,5</td><td>10,0</td><td>7,5</td><td>6,0</td><td>8,0</td><td>6,5</td></tr>
<tr class="data"><td class="label">Stärke + Zucker<span>%</span></td><td>27-30</td><td>12-15</td><td>8-11</td><td>12-15</td><td>10-13</td><td>12-15</td><td>12-15</td><td>10-13</td><td>10-13</td><td>10-13</td><td>10-13</td><td>12-15</td><td>12-15</td></tr>
<tr class="data"><td class="label">Calcium<span>%</span></td><td>0,40</td><td>0,35</td><td>0,70</td><td>0,60</td><td>0,60</td><td>0,40</td><td>0,50</td><td>0,60</td><td>0,60</td><td>0,55</td><td>0,45</td><td>0,55</td><td>0,50</td></tr>
<tr class="data"><td class="label">Phosphor<span>%</span></td><td>0,50</td><td>0,90</td><td>1,05</td><td>0,75</td><td>1,00</td><td>0,90</td><td>1,00</td><td>0,95</td><td>1,00</td><td>0,90</td><td>0,85</td><td>0,90</td><td>0,85</td></tr>
<tr class="data"><td class="label">Natrium<span>%</span></td><td>0,10</td><td>0,10</td><td>0,10</td><td>0,10</td><td>0,10</td><td>0,10</td><td>0,10</td><td>0,10</td><td>0,10</td><td>0,05</td><td>0,05</td><td>0,05</td><td>0,05</td></tr>
<tr class="energy"><td class="label">Energie NEL<span style="padding-right:14px">MJ/kg</span></td><td>7,1</td><td>6,9</td><td>6,7</td><td>7,2</td><td>7,0</td><td>7,2</td><td>7,0</td><td>7,0</td><td>7,0</td><td>7,0</td><td>7,2</td><td>7,0</td><td>7,2</td></tr>
</table>
</div>

<footer class="footer">
  <div class="col f-brand">
    <div class="mark"></div>
    <div class="name">AUEN LANDHANDEL</div>
    <div class="addr">Lindenweg 4<br>92399 Feldheim</div>
    <div class="contacts">
      <div><span class="icon"><svg viewBox="0 0 24 24"><path fill="#fff" d="M6.6 10.8a15 15 0 0 0 6.6 6.6l2.2-2.2c.3-.3.7-.4 1-.2 1.1.4 2.3.6 3.6.6.6 0 1 .4 1 1V20c0 .6-.4 1-1 1A17 17 0 0 1 3 4c0-.6.4-1 1-1h3.5c.6 0 1 .4 1 1 0 1.3.2 2.5.6 3.6.1.3 0 .7-.2 1z"/></svg></span>09123 45 67 80</div>
      <div><span class="icon"><svg viewBox="0 0 24 24"><rect x="3" y="6" width="18" height="12" fill="none" stroke="#fff" stroke-width="2"/><path d="M3 6l9 7 9-7" fill="none" stroke="#fff" stroke-width="2"/></svg></span>info@auen-landhandel.de</div>
      <div><span class="icon"><svg viewBox="0 0 24 24"><rect x="7" y="2" width="10" height="20" rx="2" fill="none" stroke="#fff" stroke-width="2.4"/></svg></span>0171 234 56 78</div>
      <div><span class="icon"><svg viewBox="0 0 24 24"><circle cx="12" cy="12" r="9" fill="none" stroke="#fff" stroke-width="2"/><path d="M3 12h18M12 3c3 3 3 15 0 18M12 3c-3 3-3 15 0 18" fill="none" stroke="#fff" stroke-width="1.6"/></svg></span>www.auen-landhandel.de</div>
    </div>
  </div>
  <div class="col f-info">
    <h2>INFORMATIONEN</h2>
    <ul><li>Downloads</li><li>Partner</li><li>Kontakt</li></ul>
    <ul><li>AGB</li><li>Datenschutz</li><li>Impressum</li></ul>
  </div>
  <div class="col f-about">
    <h2>ÜBER UNS</h2>
    <p>Wir von Auen Landhandel sind ein Familienunternehmen für Einzel- und Mischfutter. Unsere jahrelange Erfahrung durch unseren eigenen Milchviehbetrieb zeigt uns, wie wichtig hochwertige Nahrung für das Tierwohlbefinden ist. Dieses Wissen wollen wir an unsere Kunden weitergeben.</p>
  </div>
</footer>
<div class="copyright">©2023 Auen Landhandel</div>
</body>
</html>
```